charity helping airline passengers needs web site design

We need a website design (and a logo) for a new charity based in Switzerland. We are helping airline passengers to receive the compensation they are entiteld to by european law from the airlines in cases of delays or denied boarding or cancelled flights. Airlines often try to not pay those compensations so the passengers need assistance in receiving the compensations.

Target Market(s)

Switzerland

Industry/Entity Type

Charity

Logo Text

lindenkrügelhof.ch

Number of Pages Required

1 page

Colors

Designer to choose colors to be used in the design.

```html
<!DOCTYPE html>
<html lang="en">
<head>
<meta charset="utf-8">
<title>lindenkrügelhof.ch – Passenger Compensation</title>
<link href="https://fonts.googleapis.com/css2?family=Mulish:wght@400;600;700;800&family=Open+Sans:wght@400;600&display=swap" rel="stylesheet">
<style>
:root{
  --blue:#1e8fe6;
  --blue-deep:#0f6fd6;
  --blue-light:#2ba9f2;
  --orange:#f7941d;
  --ink:#222;
  --text:#555;
  --muted:#777;
  --line:#d8d8d8;
  --white:#fff;
}
*{box-sizing:border-box;margin:0;padding:0}
html,body{width:1200px;height:3010px;overflow:hidden;background:var(--white)}
body{position:relative;font-family:"Open Sans",Arial,sans-serif;color:var(--text)}
.abs{position:absolute}
.brand{font-family:"Mulish",Arial,sans-serif;font-weight:800;color:var(--ink);letter-spacing:-.5px;white-space:nowrap}

/* header */
.site-header{left:0;top:0;width:1200px;height:100px;background:var(--white)}
.site-header .brand{left:115px;top:28px;font-size:32px}
.main-nav{right:124px;top:0;height:100px;display:flex;gap:36px;align-items:center;list-style:none;font-family:"Mulish",sans-serif;font-size:17px;color:var(--ink)}
.main-nav li{position:relative;height:100px;display:flex;align-items:center}
.main-nav li.active{color:var(--blue)}
.main-nav li.active::after{content:"";position:absolute;left:-4px;right:-4px;bottom:0;height:5px;background:var(--blue)}

/* hero */
.hero{left:0;top:100px;width:1200px;height:568px;background:linear-gradient(180deg,#9aa7b4 0%,#c7ccd2 28%,#6f7f70 55%,#3f5a2f 78%,#4a4a3a 100%)}
.hero-title{left:0;top:178px;width:1200px;text-align:center;font-family:"Mulish",sans-serif;font-weight:600;font-size:38px;line-height:46px;color:var(--white)}
.btn-outline{display:flex;align-items:center;justify-content:center;border:2px solid var(--white);color:var(--white);font-family:"Mulish",sans-serif;font-size:15px;font-weight:600;letter-spacing:.5px}
.hero .btn-outline{left:522px;top:290px;width:158px;height:44px}
.hero-dots{left:532px;top:530px;display:flex;gap:8px}
.hero-dots span{width:14px;height:14px;border-radius:50%;background:var(--white)}
.hero-dots span.current{background:transparent;border:2px solid var(--white)}

/* about */
.about-photo{left:0;top:790px;width:1200px;height:470px;clip-path:polygon(0 0,100% 0,100% 82%,0 100%);background:linear-gradient(180deg,#ffffff 0%,#dfe3e8 18%,#a9acaa 45%,#7b7a72 75%,#5d5d58 100%)}
.section-title{font-family:"Mulish",sans-serif;font-weight:600;color:var(--ink)}
.about-title{left:0;top:718px;width:1200px;text-align:center;font-size:34px}
.about-text{left:220px;width:760px;text-align:center;font-size:15px;line-height:21px;color:var(--muted)}
.btn-solid{display:flex;align-items:center;justify-content:center;background:var(--orange);color:var(--white);font-family:"Mulish",sans-serif;font-size:16px;font-weight:600}
.about .btn-solid{left:518px;top:910px;width:166px;height:44px}

/* services */
.services{left:0;top:1180px;width:1200px;height:580px;clip-path:polygon(0 14%,100% 0,100% 100%,0 92%)}
.services-photo{left:0;top:0;width:1200px;height:580px;background:linear-gradient(90deg,#8a97a6 0%,#b9c1c9 45%,#3a63b4 72%,#2c2f3b 100%)}
.services-band{left:0;top:0;width:1200px;height:580px;background:linear-gradient(90deg,var(--blue-deep) 0%,var(--blue-light) 34%,rgba(43,169,242,.55) 48%,rgba(43,169,242,0) 62%)}
.services-title{left:118px;top:148px;font-family:"Mulish",sans-serif;font-size:29px;color:var(--white)}
.services-text{left:118px;top:198px;width:400px;font-size:14px;line-height:21px;color:var(--white)}
.services-list{left:118px;top:276px;list-style:none;font-size:14px;color:var(--white)}
.services-list li{height:33px;display:flex;align-items:center;gap:10px}
.services .btn-outline{left:124px;top:390px;width:154px;height:42px;font-size:14px}

/* news */
.news-title{left:120px;top:1756px;font-size:29px}
.news-card{top:1822px;width:472px;height:222px;border:1px solid var(--line);background:var(--white)}
.news-card .thumb{left:0;top:0;width:234px;height:220px}
.news-card .date{left:0;top:0;width:58px;height:58px;background:var(--blue-deep);color:var(--white);text-align:center;font-family:"Mulish",sans-serif;line-height:1}
.news-card .date b{display:block;font-size:21px;font-weight:600;padding-top:8px}
.news-card .date i{font-style:normal;font-size:13px}
.news-card h3{left:258px;top:26px;width:196px;font-family:"Mulish",sans-serif;font-weight:600;font-size:15px;line-height:20px;color:var(--blue-deep)}
.news-card p{left:258px;top:84px;width:190px;font-size:12px;line-height:19px;color:var(--muted)}
.news-card .more{left:258px;top:176px;font-family:"Mulish",sans-serif;font-weight:600;font-size:13px;color:var(--ink)}

/* why */
.why{left:0;top:2122px;width:1200px;height:516px;clip-path:polygon(0 10%,100% 0,100% 100%,0 92%);background:linear-gradient(90deg,#3b3e45 0%,#6a6a66 35%,#5a5550 60%,#34383f 100%)}
.why-shade{left:0;top:0;width:1200px;height:516px;background:rgba(20,24,30,.35)}
.why-title{left:0;top:154px;width:1200px;text-align:center;font-family:"Mulish",sans-serif;font-size:31px;color:var(--white)}
.why-text{left:230px;width:740px;text-align:center;font-size:15px;line-height:21px;color:var(--white)}
.why .btn-outline{left:508px;top:334px;width:178px;height:42px;font-size:14px}

/* footer */
.site-footer .brand{left:128px;top:2700px;font-size:23px}
.footer-col{top:2686px;font-family:"Mulish",sans-serif}
.footer-col h4{font-size:19px;font-weight:600;color:var(--ink);margin-bottom:14px}
.footer-col ul{list-style:none;font-family:"Open Sans",sans-serif;font-size:14px;color:var(--text)}
.footer-col li{height:30px}
.social{display:flex;gap:8px}
.social span{width:32px;height:32px;border:2px solid var(--blue);border-radius:50%}
.footer-rule{left:116px;top:2932px;width:964px;height:1px;background:var(--line)}
.copyright{left:0;top:2950px;width:1200px;text-align:center;font-size:12px;color:var(--muted)}
</style>
</head>
<body>

<header class="site-header abs">
  <div class="brand abs">lindenkrügelhof.ch</div>
  <ul class="main-nav abs">
    <li class="active">Home</li><li>About Us</li><li>Services</li><li>Mission</li><li>News</li><li>Blog</li><li>Contact</li>
  </ul>
</header>

<section class="hero abs" role="img" aria-label="Swiss alpine village with a church tower beneath snow-capped mountains">
  <h1 class="hero-title abs">We are Helping Airline Passengers<br>to Receive the Compensation</h1>
  <div class="btn-outline abs">LEARN MORE</div>
  <div class="hero-dots abs"><span class="current"></span><span></span><span></span><span></span></div>
</section>

<section class="about">
  <div class="about-photo abs" role="img" aria-label="Airport apron with passenger jets parked at the gates"></div>
  <h2 class="section-title about-title abs">About lindenkrügelhof.ch</h2>
  <p class="about-text abs" style="top:784px">commodo a mi Morbi ornare gravida elit Integer congue augue et malesuada iaculis ipsum dui aliquet felis at cursus magna nisl nec elit Praesent elementum elit</p>
  <p class="about-text abs" style="top:840px">sit amet porttitor mattis enim In massa libero interdum nec interdum vel blandit sed nulla In ullamcorper est eget tempor cursus neque mi consectetuer mi a ultricies massa est sed nisl Class aptent t</p>
  <div class="btn-solid abs">LEARN MORE</div>
</section>

<section class="services abs">
  <div class="services-photo abs" role="img" aria-label="Frustrated traveller sitting beside his suitcase in an airport lounge"></div>
  <div class="services-band abs"></div>
  <h2 class="services-title abs">Services Provides</h2>
  <p class="services-text abs">Praesent elementum elit at tellus nec ultricies sit amet porttitor mattis enim In massa libero interdum nec interdum vel blandit sed nulla In ullamco</p>
  <ul class="services-list abs">
    <li><svg width="8" height="10" viewBox="0 0 8 10"><path d="M2 1l4 4-4 4" fill="none" stroke="#fff" stroke-width="1.5"/></svg>Cases of Delays</li>
    <li><svg width="8" height="10" viewBox="0 0 8 10"><path d="M2 1l4 4-4 4" fill="none" stroke="#fff" stroke-width="1.5"/></svg>Denied Boarding</li>
    <li><svg width="8" height="10" viewBox="0 0 8 10"><path d="M2 1l4 4-4 4" fill="none" stroke="#fff" stroke-width="1.5"/></svg>Cancelled Flights</li>
  </ul>
  <div class="btn-outline abs">LEARN MORE</div>
</section>

<h2 class="section-title news-title abs">News &amp; Blogs</h2>

<article class="news-card abs" style="left:116px">
  <div class="thumb abs" role="img" aria-label="Travellers in an airport hall below a departures board" style="background:linear-gradient(180deg,#4d6f9a 0%,#9aa9b8 45%,#c9b8a0 100%)"></div>
  <div class="date abs"><b>29</b><i>JUL</i></div>
  <h3 class="abs">Class aptent taciti soci osquad litora torq</h3>
  <p class="abs">conubia nostra per inceptos hymenaeos Proin nulla arcu nonummy luctus dictum eget fermentum et lorem</p>
  <div class="more abs">READ MORE</div>
</article>

<article class="news-card abs" style="left:608px">
  <div class="thumb abs" role="img" aria-label="Couple with travel documents in front of an aircraft" style="background:linear-gradient(90deg,#e9ecef 0%,#d8c4b4 45%,#b98f83 70%,#eef0f2 100%)"></div>
  <div class="date abs"><b>29</b><i>JUL</i></div>
  <h3 class="abs">Class aptent taciti soci osquad litora torq</h3>
  <p class="abs">conubia nostra per inceptos hymenaeos Proin nulla arcu nonummy luctus dictum eget fermentum et lorem</p>
  <div class="more abs">READ MORE</div>
</article>

<section class="why abs" role="img" aria-label="Passenger waiting with her phone in a busy airport terminal">
  <div class="why-shade abs"></div>
  <h2 class="why-title abs">Why We Are</h2>
  <p class="why-text abs" style="top:206px">Lernwerk is a cloud-based platform that delivers a quick, effective micro-learning solution for corporate training.&nbsp; We accelerate user adoption of new technologies and processes</p>
  <p class="why-text abs" style="top:262px">Lernwerk also creates unique, custom content such as sales skills, product info, privacy policies,<br>business applications and employee onboarding.</p>
  <div class="btn-outline abs">LEARN MORE</div>
</section>

<footer class="site-footer">
  <div class="brand abs">lindenkrügelhof.ch</div>
  <div class="footer-col abs" style="left:388px"><h4>Company</h4><ul><li>Home</li><li>About Us</li><li>What We Do</li><li>Our Mission</li></ul></div>
  <div class="footer-col abs" style="left:582px"><h4>Solutions</h4><ul><li>Our Services</li><li>Team</li><li>Blogs</li><li>News</li></ul></div>
  <div class="footer-col abs" style="left:762px"><h4>Resources</h4><ul><li>Case Studies</li><li>Contact</li><li>Term of Use</li></ul></div>
  <div class="footer-col abs" style="left:930px"><h4>Follow Us</h4><div class="social"><span></span><span></span><span></span><span></span></div></div>
  <div class="footer-rule abs"></div>
  <p class="copyright abs">© 2017 Company Name&nbsp; All right reserved</p>
</footer>

</body>
</html>
```